Round Label Sticker 2.5-3 inch diameter

We need a design for a sticker to distribute for more brand recognition and product outreach.
My company The Bright Plate Company Ltd. Specializes in working with people with diabetes. My products are made for diabetics because they have no added sugars, high in protein and fiber and each serving is lower than 5% daily value of carbohydrates.
I am a dietitian and my dad passed away from diabetes. I have created a growing food and beverage line that will give more joy into a diabetic's life while providing more food options that make them feel happy instead of guilty when they eat it.
I am teaching cooking classes to promote my products as well as doing exhibits and events. I want to give away a sticker to people that reads "I'm too sweet for sugar!" and somewhere on it would be my logo as well as my website info. www.brightplate.example
The sticker should make people smile and warm as well as draw interest to my product line.
Target Market(s)
Diabetes and people who do not want added sugars in their food
Industry/Entity Type
Food Store
Requirements
Must have
- my logo and website

```html
<!DOCTYPE html>
<html lang="en">
<head>
<meta charset="utf-8">
<title>Bright Plate – I'm too sweet for sugar! sticker</title>
<link rel="stylesheet" href="https://fonts.googleapis.com/css2?family=Lobster&family=Great+Vibes&family=Nunito:wght@600&display=swap">
<style>
  :root {
    --page: #ffffff;
    --sticker-edge: #1a1a1a;
    --sticker-paper: #fdfcfb;
    --headline-magenta: #c4177f;
    --brand-purple: #5a2a8a;
    --brand-green: #7dbd3c;
    --art-purple: #8a5aae;
    --art-green: #b7d97a;
    --confetti-warm: rgba(240, 150, 90, 0.18);
    --confetti-cool: rgba(90, 150, 210, 0.16);
    --confetti-pink: rgba(230, 120, 170, 0.14);
  }
  html, body {
    margin: 0;
    padding: 0;
    width: 1200px;
    height: 1200px;
    overflow: hidden;
    background: var(--page);
  }
  .canvas {
    position: relative;
    width: 1200px;
    height: 1200px;
  }
  .sticker {
    position: absolute;
    left: 100px;
    top: 100px;
    width: 1000px;
    height: 1000px;
    border-radius: 50%;
    border: 2px solid var(--sticker-edge);
    box-sizing: border-box;
    background: var(--sticker-paper);
    overflow: hidden;
  }
  .sticker__confetti {
    position: absolute;
    inset: 0;
    background:
      radial-gradient(ellipse 70% 35% at 50% 92%, var(--confetti-warm), transparent 70%),
      radial-gradient(ellipse 40% 30% at 15% 75%, var(--confetti-cool), transparent 70%),
      radial-gradient(ellipse 40% 30% at 88% 70%, var(--confetti-pink), transparent 70%),
      radial-gradient(ellipse 60% 25% at 45% 8%, var(--confetti-pink), transparent 70%);
  }
  .brand {
    position: absolute;
    left: 570px;
    top: 318px;
    width: 370px;
    text-align: center;
  }
  .brand__name {
    display: block;
    font-family: "Lobster", cursive;
    font-size: 64px;
    line-height: 1;
    white-space: nowrap;
    color: var(--brand-purple);
  }
  .brand__rule {
    display: block;
    width: 330px;
    height: 3px;
    margin: 42px auto 8px;
    background: var(--brand-green);
  }
  .brand__web {
    display: block;
    font-family: "Nunito", sans-serif;
    font-weight: 600;
    font-size: 27px;
    white-space: nowrap;
    color: var(--brand-green);
    letter-spacing: 0.5px;
  }
  .mascot-art {
    position: absolute;
    left: 160px;
    top: 362px;
    width: 370px;
    height: 330px;
    border-radius: 24px;
    background: linear-gradient(135deg, var(--art-purple), var(--art-green));
    opacity: 0.55;
  }
  .headline {
    position: absolute;
    inset: 0;
    color: var(--headline-magenta);
    margin: 0;
    font-weight: 400;
  }
  .headline__lead,
  .headline__key,
  .headline__tail {
    position: absolute;
    white-space: nowrap;
    line-height: 1;
  }
  .headline__lead {
    left: 212px;
    top: 718px;
    font-family: "Lobster", cursive;
    font-size: 118px;
    transform: rotate(-6deg);
    transform-origin: left center;
  }
  .headline__key {
    left: 565px;
    top: 560px;
    font-family: "Great Vibes", cursive;
    font-size: 225px;
    transform: rotate(-4deg);
  }
  .headline__tail {
    left: 415px;
    top: 815px;
    font-family: "Lobster", cursive;
    font-size: 104px;
    transform: rotate(-4deg);
  }
</style>
</head>
<body>
  <main class="canvas">
    <section class="sticker">
      <div class="sticker__confetti" role="img" aria-label="Soft watercolour confetti dots scattered across the sticker"></div>
    </section>

    <div class="brand">
      <span class="brand__name">Bright Plate</span>
      <span class="brand__rule"></span>
      <span class="brand__web">www.brightplate.example</span>
    </div>

    <div class="mascot-art" role="img" aria-label="Cheerful cartoon donut mascot with purple sprinkled icing and green dough, arms raised"></div>

    <h1 class="headline">
      <span class="headline__lead">I'm too</span>
      <span class="headline__key">Sweet</span>
      <span class="headline__tail">for sugar!</span>
    </h1>
  </main>
</body>
</html>
```